Comic, writer, and entrepreneur based in Los Angeles, CA

UPDATED BRIEF:

Need a PROFESSIONAL yet simultaneously sexy business card that will inspire those to go to my social media accounts and follow me.

Need all of my social media (logos on card, please) As well as my picture, which I will provide.

If there is a way where you could scan the business card from your phone and it would take you to the social media accounts that would be great too!

My goal is to get a comedy writing job at the Evening Desk or LNB and also go on Otter Pond once my app is fully functional and created.

But the business card is just something to give people when I am making connections in both the entrepreneurial world as well as the comedy world so it has to help me stand out in that way :).

#: 555-284-7193
Email: kbellamy@mail.northfen.edu
Snapgrid: Korinne_Q.P
Chirpline: @ThePelicanLedger
Crafterly: Kori’s Quirky Tops (website: https://www.crafterly-example.com/shop/KorisTp?ref=pr_shop_more)
ClipCastle: The Gagsmith (website: https://www.clipcastle-example.com/channel/QWzRtp4nL-vbKJyymu7gfe9B )
Friendwall: /korinne.bellamy.71204
Website App: QuickFixPals.net (app in progress. Need emails to make a prototype.)

Target Market(s)

Talent agents needing TV writers and TV comedy personalities. Investors for my app.

Industry/Entity Type

Tv

Contact Information for Business Card

Can be double or single sided, whichever looks best. Green is my favorite color but I am open to anything. Maybe silver and green?! Just make it classy and sexy.

Colors

Designer to choose colors to be used in the design.

Requirements
Must have
• Chirpline: ThePelicanLedger
• Snapgrid: Korinne_q.p
• Clipcastle: The Gagsmith
• Email: kbellamy@mail.northfen.edu
• Phone: 555-284-7193
• writer, comic, entrepreneur--or--comedy writer and entrepeneur
Nice to have
• Make me standout. I'm a star ;-). Please check out my social media for files or ideas. Thanks.

```html
<!DOCTYPE html>
<html lang="en">
<head>
<meta charset="utf-8">
<title>Business Card – Korinne Bellamy</title>
<link rel="stylesheet" href="https://fonts.googleapis.com/css2?family=Arimo:wght@400;700&family=Roboto+Condensed:wght@400&display=swap">
<style>
  :root {
    --page: #e9edf0;
    --green: #41bc94;
    --pink: #e8097a;
    --crimson: #a8152f;
    --blush: #f8bfd8;
    --cream: #fdf6a2;
    --ink: #111111;
    --white: #ffffff;
  }
  html, body {
    margin: 0;
    width: 1200px;
    height: 882px;
    overflow: hidden;
    background: var(--page);
  }
  .business-card {
    position: absolute;
    left: 105px;
    top: 143px;
    width: 990px;
    height: 595px;
    box-shadow: 0 18px 40px rgba(40, 50, 60, 0.35);
  }
  .business-card svg { display: block; width: 100%; height: 100%; }
  .name { font-family: "Arimo", Arial, sans-serif; font-weight: 700; font-size: 19px; fill: var(--white); }
  .role { font-family: "Arimo", Arial, sans-serif; font-size: 14px; fill: var(--white); }
  .handle-light { font-family: "Arimo", Arial, sans-serif; font-size: 13.5px; fill: var(--white); }
  .contact { font-family: "Arimo", Arial, sans-serif; font-size: 14px; fill: var(--ink); }
  .contact-condensed { font-family: "Roboto Condensed", "Arial Narrow", sans-serif; font-size: 13.5px; fill: var(--ink); }
  .contact-small { font-family: "Roboto Condensed", "Arial Narrow", sans-serif; font-size: 14px; fill: var(--ink); }
  .phone-number { font-family: "Arimo", Arial, sans-serif; font-size: 15px; letter-spacing: 3.2px; fill: var(--white); }
</style>
</head>
<body>
<div class="business-card">
  <svg viewBox="0 0 521 313" xmlns="http://www.w3.org/2000/svg">
    <defs>
      <linearGradient id="band-top" x1="0" y1="0" x2="0" y2="1">
        <stop offset="0" stop-color="#b3183a"/>
        <stop offset="0.22" stop-color="#e8097a"/>
        <stop offset="1" stop-color="#e8097a"/>
      </linearGradient>
      <linearGradient id="band-phone" x1="0" y1="0" x2="0" y2="1">
        <stop offset="0" stop-color="#e8097a"/>
        <stop offset="0.5" stop-color="#d50d5a"/>
        <stop offset="1" stop-color="#a8152f"/>
      </linearGradient>
      <linearGradient id="portrait-tone" x1="0" y1="0" x2="1" y2="1">
        <stop offset="0" stop-color="#c9a271"/>
        <stop offset="0.45" stop-color="#e7bfa0"/>
        <stop offset="0.8" stop-color="#c9b9a6"/>
        <stop offset="1" stop-color="#2c3f9a"/>
      </linearGradient>
    </defs>

    <rect class="card-base" x="0" y="0" width="521" height="313" fill="var(--green)"/>

    <polygon class="portrait" role="img" aria-label="Portrait photo of the card owner"
             points="0,78 205,78 270,313 68,313" fill="url(#portrait-tone)"/>

    <polygon class="contact-panel" points="205,85 521,85 521,242 250,242" fill="var(--cream)"/>

    <polygon class="name-band" points="0,19 283,19 305,78 0,78" fill="url(#band-top)"/>
    <polygon class="name-band-accent" points="287,24 300,24 330,78 315,78" fill="var(--blush)"/>
    <text class="name" x="37" y="49">Your Name</text>
    <text class="role" x="37" y="69">Positions</text>

    <text class="handle-light" x="463" y="66" text-anchor="end">@ThePelicanLedger</text>
    <rect x="469" y="48" width="25" height="25" fill="var(--white)"/>
    <rect x="472" y="51" width="19" height="19" fill="var(--green)"/>

    <g class="contact-list">
      <text class="contact" x="463" y="106" text-anchor="end">Korinne_Q.P</text>
      <rect x="469" y="89" width="25" height="25" fill="var(--crimson)"/>
      <rect x="472" y="92" width="19" height="19" fill="var(--pink)"/>

      <text class="contact-condensed" x="463" y="136" text-anchor="end">/channel/QWzRtp4nL-vbKJyymu7gfe9B</text>
      <rect x="469" y="119" width="25" height="25" fill="var(--crimson)"/>
      <rect x="472" y="122" width="19" height="19" fill="var(--pink)"/>

      <text class="contact" x="463" y="167" text-anchor="end">kbellamy@mail.northfen.edu</text>
      <rect x="469" y="149" width="25" height="25" fill="var(--crimson)"/>
      <rect x="472" y="152" width="19" height="19" fill="var(--pink)"/>
      <g class="icon-mail" fill="none" stroke="var(--white)" stroke-width="1.2">
        <rect x="475.5" y="157" width="12" height="9"/>
        <polyline points="475.5,157 481.5,162 487.5,157"/>
      </g>

      <text class="contact" x="463" y="197" text-anchor="end">/korinne.bellamy.71204</text>
      <rect x="469" y="179" width="25" height="25" fill="var(--crimson)"/>
      <rect x="472" y="182" width="19" height="19" fill="var(--pink)"/>

      <text class="contact-small" x="463" y="218" text-anchor="end">https://www.crafterly-example.com/shop/</text>
      <text class="contact-small" x="463" y="233" text-anchor="end">KorisTp?ref=pr_shop_more</text>
      <rect x="469" y="209" width="25" height="25" fill="var(--crimson)"/>
      <rect x="472" y="212" width="19" height="19" fill="var(--pink)"/>
      <g class="icon-globe" fill="none" stroke="var(--white)" stroke-width="1.1">
        <circle cx="481.5" cy="221.5" r="6.5"/>
        <ellipse cx="481.5" cy="221.5" rx="3" ry="6.5"/>
        <line x1="475" y1="221.5" x2="488" y2="221.5"/>
      </g>
    </g>

    <polygon class="phone-band" points="0,249 345,249 368,302 0,302" fill="url(#band-phone)"/>
    <polygon class="phone-band-accent" points="350,249 362,249 386,302 373,302" fill="var(--blush)"/>
    <rect x="69" y="262" width="26" height="26" fill="var(--white)"/>
    <rect x="72" y="265" width="20" height="20" fill="var(--crimson)"/>
    <path class="icon-phone" fill="var(--white)"
          d="M76.5,269 l3,-1 l2,4 l-2,1.5 c0.8,2 2.3,3.5 4.3,4.3 l1.5,-2 l4,2 l-1,3 c-6,0.5 -12.3,-5.8 -11.8,-11.8z"/>
    <text class="phone-number" x="108" y="279">555-284-7193</text>
  </svg>
</div>
</body>
</html>
```